Professional Website

We are looking for a new website for our Staffing Company. Attached is a document with all the details and pages needed along with some examples of others websites.

We want a professional Look and feel around the same color theme as the attached Vivid Vision.

We currently host our site on Pagecraft.io. If the winning designer can also add to Pagecraft, that is a plus.

```html
<!DOCTYPE html>
<html lang="en">
<head>
<meta charset="utf-8">
<title>Hireway – Website Design</title>
<link href="https://fonts.googleapis.com/css2?family=Poppins:wght@400;500;600;700;800&display=swap" rel="stylesheet">
<style>
:root{
  --indigo:#2d2f9f;
  --indigo-dark:#1f2178;
  --ink:#1e1e24;
  --text:#55565f;
  --footer:#262628;
  --footer-line:#3a3a3d;
  --paper:#ffffff;
  --mist:#f1f2f7;
  --stage:#f6f6f8;
  --photo-a:#8a8f99;
  --photo-b:#c9ccd3;
}
*{box-sizing:border-box;margin:0;padding:0}
html,body{width:1200px;height:2660px;overflow:hidden}
body{background:var(--stage);font-family:"Poppins",sans-serif;color:var(--text)}
.canvas{position:relative;width:1200px;height:2660px;overflow:hidden}

/* ---------- desktop ---------- */
.desktop{position:absolute;left:150px;top:40px;width:900px;height:560px;background:var(--paper);box-shadow:0 10px 40px rgba(0,0,0,.14);overflow:hidden}
.topbar{background:var(--indigo-dark);color:#fff;font-size:9px;text-align:center;padding:4px 0;letter-spacing:.3px}
.nav{display:flex;align-items:center;justify-content:space-between;padding:12px 40px;background:#fff}
.brand{font-weight:800;color:var(--indigo);font-size:24px;letter-spacing:-.5px}
.nav-links{display:flex;gap:24px;font-size:11px;color:var(--ink);font-weight:500;align-items:center}
.nav-btn{background:var(--indigo);color:#fff;padding:7px 14px;border-radius:3px;font-weight:600}
.hero{position:relative;height:470px;background:linear-gradient(160deg,#6d7480,#b8bcc4 55%,#8f949d);}
.hero-shade{position:absolute;inset:0;background:linear-gradient(180deg,rgba(20,20,40,.15),rgba(20,20,40,.35))}
.hero-copy{position:absolute;left:0;right:0;top:150px;text-align:center;color:#fff}
.hero-copy h1{font-size:42px;font-weight:700;line-height:1.1;text-shadow:0 2px 8px rgba(0,0,0,.3)}
.hero-actions{display:flex;justify-content:center;gap:14px;margin-top:22px}
.btn{font-size:10px;font-weight:700;padding:9px 18px;border-radius:3px;letter-spacing:.4px}
.btn-light{background:#fff;color:var(--indigo)}
.btn-solid{background:var(--indigo);color:#fff}
.swoosh{position:absolute;left:0;bottom:0;width:100%}

/* ---------- mobile ---------- */
.phone{position:absolute;top:650px;width:196px;background:var(--paper);box-shadow:0 6px 22px rgba(0,0,0,.13);overflow:hidden;font-size:6.5px;line-height:1.5}
.p1{left:50px}.p2{left:276px}.p3{left:502px}.p4{left:728px}.p5{left:954px}
.m-top{background:var(--indigo-dark);color:#fff;font-size:5px;text-align:center;padding:2px 0}
.m-nav{display:flex;justify-content:space-between;align-items:center;padding:7px 10px}
.m-brand{font-weight:800;color:var(--indigo);font-size:13px}
.burger{width:16px;height:14px;background:var(--indigo);border-radius:2px;display:flex;flex-direction:column;justify-content:center;gap:2px;padding:0 4px}
.burger span{height:1.5px;background:#fff}
.m-hero{position:relative;height:210px;background:linear-gradient(160deg,#6f7581,#b6bac3 60%,#8d929b)}
.m-hero.city{background:linear-gradient(170deg,#4f5a6a,#a3adbb 60%,#6b7584)}
.m-hero.office{background:linear-gradient(170deg,#7c8089,#cfd2d8 60%,#9a9ea6)}
.m-hero h2{position:absolute;left:10px;right:10px;top:58px;color:#fff;font-size:17px;font-weight:700;line-height:1.1;text-shadow:0 1px 5px rgba(0,0,0,.35)}
.m-hero h2.center{text-align:center}
.m-hero .m-actions{position:absolute;left:10px;top:132px;display:flex;gap:5px}
.m-btn{font-size:5px;font-weight:700;padding:4px 7px;border-radius:2px}
.m-swoosh{position:absolute;left:0;bottom:0;width:100%}
.m-form{position:absolute;left:12px;right:12px;top:96px;background:rgba(255,255,255,.95);padding:7px;border-radius:2px}
.m-field{height:11px;border:1px solid #d5d7de;margin-bottom:4px;font-size:5px;padding:1px 4px;color:#888}
.m-form .m-btn{display:inline-block;background:var(--indigo);color:#fff}
.m-photo{height:130px;margin:10px 10px 0;background:linear-gradient(135deg,var(--photo-a),var(--photo-b))}
.m-photo.warm{background:linear-gradient(135deg,#6d6a66,#d6d0c8)}
.m-photo.map{background:linear-gradient(135deg,#e7e8ec,#cfd2d9);height:140px}
.m-section{padding:12px 12px}
.m-section h3{color:var(--ink);font-size:11px;font-weight:700;text-align:center;margin-bottom:6px}
.m-section p{text-align:center;margin-bottom:6px}
.m-list{list-style:none;margin:4px 0 6px;text-align:center}
.m-list li{margin-bottom:2px}
.ticks{list-style:none}
.ticks li{display:flex;gap:5px;margin-bottom:5px;align-items:flex-start}
.tick{flex:0 0 7px;height:7px;border-radius:50%;background:var(--indigo);margin-top:1px}
.m-center{text-align:center}
.m-center .m-btn{display:inline-block;background:var(--indigo);color:#fff}
.benefits{display:grid;grid-template-columns:1fr 1fr;gap:6px;margin-top:4px}
.benefit{border:1px solid #dcdfe8;padding:6px 5px;display:flex;gap:4px;align-items:center;font-size:5.5px;color:var(--ink);font-weight:600}
.b-icon{flex:0 0 10px;height:10px;background:var(--indigo);border-radius:2px}
.cards{display:grid;grid-template-columns:1fr 1fr;gap:6px}
.card{height:62px;background:linear-gradient(135deg,#5d6473,#b7bcc6);position:relative}
.card span{position:absolute;left:0;right:0;bottom:0;background:var(--indigo);color:#fff;font-size:5px;font-weight:600;padding:2px 4px}
.offices{list-style:none;text-align:center}
.offices li{margin-bottom:8px}
.offices b{display:block;color:var(--ink);font-size:7px}
.band{background:var(--mist)}

/* footer */
.m-foot{background:var(--footer);color:#bfc0c6;padding:14px 12px 0;text-align:center}
.m-foot .m-brand{color:#fff;display:block;margin-bottom:6px}
.m-foot h4{color:#fff;font-size:8px;margin:10px 0 4px}
.m-foot ul{list-style:none}
.m-foot li{margin-bottom:2px}
.socials{display:flex;justify-content:center;gap:5px;margin:10px 0 12px}
.socials span{width:11px;height:11px;border-radius:50%;background:#4a4a4f}
.m-copy{background:var(--indigo);color:#fff;font-size:5px;margin:0 -12px;padding:4px 0}
</style>
</head>
<body>
<div class="canvas">

  <section class="desktop">
    <div class="topbar">Proudly Serving Employers &amp; Job Seekers Nationwide</div>
    <header class="nav">
      <div class="brand">Hireway</div>
      <nav class="nav-links">
        <span>Employers</span><span>Job Seekers</span><span>Contact Us</span>
        <span class="nav-btn">1-800-555-0147</span>
      </nav>
    </header>
    <div class="hero">
      <div class="hero-shade" role="img" aria-label="Team of smiling office professionals standing in a bright modern office"></div>
      <div class="hero-copy">
        <h1>Dream Jobs. Top Talent. All In One Place.</h1>
        <div class="hero-actions">
          <span class="btn btn-light">FIND A NEW CAREER</span>
          <span class="btn btn-solid">EXPLORE EMPLOYERS</span>
        </div>
      </div>
      <svg class="swoosh" viewBox="0 0 900 60" preserveAspectRatio="none" height="60"><path d="M0 60 L0 30 Q450 70 900 0 L900 60 Z" fill="#2d2f9f"/><path d="M0 60 L0 48 Q450 78 900 26 L900 60 Z" fill="#fff"/></svg>
    </div>
  </section>

  <!-- home -->
  <section class="phone p1">
    <div class="m-top">Serving Employers &amp; Job Seekers</div>
    <div class="m-nav"><span class="m-brand">Hireway</span><span class="burger"><span></span><span></span><span></span></span></div>
    <div class="m-hero" role="img" aria-label="Team of office professionals">
      <h2>Dream Jobs. Top Talent. All In One Place.</h2>
      <div class="m-actions"><span class="m-btn btn-light">FIND A CAREER</span><span class="m-btn btn-solid">EMPLOYERS</span></div>
      <svg class="m-swoosh" viewBox="0 0 196 24" preserveAspectRatio="none" height="24"><path d="M0 24 L0 12 Q98 28 196 0 L196 24 Z" fill="#2d2f9f"/><path d="M0 24 L0 19 Q98 32 196 10 L196 24 Z" fill="#fff"/></svg>
    </div>
    <div class="m-photo warm" role="img" aria-label="Team members joining hands in the center"></div>
    <div class="m-section">
      <h3>About Us</h3>
      <p>Hireway connects driven people with growing companies. For over a decade we have matched skilled workers to roles that fit their goals and our clients' needs.</p>
      <p>Our recruiters know local markets and treat every placement as a lasting partnership.</p>
      <div class="m-center"><span class="m-btn">LEARN MORE</span></div>
    </div>
    <footer class="m-foot">
      <span class="m-brand">Hireway</span>
      <p>Trusted staffing partner for businesses and job seekers across the region.</p>
      <h4>Quick Links</h4>
      <ul><li>Home</li><li>Employers</li><li>Job Seekers</li><li>Locations</li><li>Contact Us</li></ul>
      <h4>Areas We Serve</h4>
      <ul><li>Brookfield</li><li>Lakeside</li><li>Millbrook</li></ul>
      <div class="socials"><span></span><span></span><span></span><span></span></div>
      <div class="m-copy">© 2024 Hireway. All rights reserved.</div>
    </footer>
  </section>

  <!-- employers -->
  <section class="phone p2">
    <div class="m-top">Serving Employers &amp; Job Seekers</div>
    <div class="m-nav"><span class="m-brand">Hireway</span><span class="burger"><span></span><span></span><span></span></span></div>
    <div class="m-hero city" role="img" aria-label="City street scene">
      <h2 class="center" style="top:30px">What type of job are you looking for?</h2>
      <div class="m-form">
        <div class="m-field">Job category</div>
        <div class="m-field">Location</div>
        <span class="m-btn">SEARCH JOBS</span>
      </div>
    </div>
    <div class="m-photo" role="img" aria-label="Group of professionals in business attire"></div>
    <div class="m-section">
      <h3>Our Services</h3>
      <p>We provide flexible staffing built around your timeline, budget and culture.</p>
      <ul class="m-list"><li>Temporary Staffing</li><li>Temp-to-Hire</li><li>Direct Hire</li><li>Payroll Services</li><li>Executive Search</li><li>Onsite Management</li></ul>
      <div class="m-center"><span class="m-btn">REQUEST STAFF</span></div>
    </div>
    <div class="m-photo warm" role="img" aria-label="Hands typing on a laptop"></div>
    <div class="m-section">
      <h3>Referral Bonus</h3>
      <p>Know someone great? Refer them to us and earn a bonus once they complete their first weeks on assignment.</p>
      <ul class="ticks">
        <li><span class="tick"></span>Refer friends, family or former coworkers.</li>
        <li><span class="tick"></span>Bonus paid after forty worked days.</li>
        <li><span class="tick"></span>No limit on the number of referrals.</li>
      </ul>
    </div>
    <div class="m-section band">
      <h3>Benefits</h3>
      <div class="benefits">
        <div class="benefit"><span class="b-icon"></span>Weekly Pay</div>
        <div class="benefit"><span class="b-icon"></span>Health Plans</div>
        <div class="benefit"><span class="b-icon"></span>Paid Holidays</div>
        <div class="benefit"><span class="b-icon"></span>Training</div>
      </div>
    </div>
    <footer class="m-foot">
      <span class="m-brand">Hireway</span>
      <p>Trusted staffing partner for businesses and job seekers across the region.</p>
      <h4>Quick Links</h4>
      <ul><li>Home</li><li>Employers</li><li>Job Seekers</li><li>Locations</li><li>Contact Us</li></ul>
      <h4>Areas We Serve</h4>
      <ul><li>Brookfield</li><li>Lakeside</li><li>Millbrook</li></ul>
      <div class="socials"><span></span><span></span><span></span><span></span></div>
      <div class="m-copy">© 2024 Hireway. All rights reserved.</div>
    </footer>
  </section>

  <!-- job seekers -->
  <section class="phone p3">
    <div class="m-top">Serving Employers &amp; Job Seekers</div>
    <div class="m-nav"><span class="m-brand">Hireway</span><span class="burger"><span></span><span></span><span></span></span></div>
    <div class="m-hero city" role="img" aria-label="City skyline">
      <h2 class="center" style="top:30px">We have the following employment positions to go</h2>
      <div class="m-form" style="top:110px">
        <div class="m-field">Position</div>
        <div class="m-field">Location</div>
        <span class="m-btn">APPLY NOW</span>
      </div>
    </div>
    <div class="m-section">
      <h3>Referral Bonus</h3>
      <div class="cards">
        <div class="card" role="img" aria-label="Warehouse worker"><span>Warehouse</span></div>
        <div class="card" role="img" aria-label="Office desk"><span>Administrative</span></div>
        <div class="card" role="img" aria-label="Factory floor"><span>Manufacturing</span></div>
        <div class="card" role="img" aria-label="Customer service desk"><span>Customer Service</span></div>
      </div>
    </div>
    <div class="m-section">
      <h3>Why work us</h3>
      <ul class="ticks">
        <li><span class="tick"></span>Access to roles at top local employers.</li>
        <li><span class="tick"></span>Weekly pay with direct deposit.</li>
        <li><span class="tick"></span>Dedicated recruiter to guide your search.</li>
        <li><span class="tick"></span>Flexible shifts that fit your schedule.</li>
        <li><span class="tick"></span>Paths from temporary to permanent work.</li>
        <li><span class="tick"></span>Free skills training and career advice.</li>
      </ul>
      <div class="m-center"><span class="m-btn">APPLY TODAY</span></div>
    </div>
    <div class="m-section band">
      <h3>Benefits</h3>
      <div class="benefits">
        <div class="benefit"><span class="b-icon"></span>Weekly Pay</div>
        <div class="benefit"><span class="b-icon"></span>Health Plans</div>
        <div class="benefit"><span class="b-icon"></span>Paid Holidays</div>
        <div class="benefit"><span class="b-icon"></span>Training</div>
      </div>
    </div>
    <footer class="m-foot">
      <span class="m-brand">Hireway</span>
      <p>Trusted staffing partner for businesses and job seekers across the region.</p>
      <h4>Quick Links</h4>
      <ul><li>Home</li><li>Employers</li><li>Job Seekers</li><li>Locations</li><li>Contact Us</li></ul>
      <h4>Areas We Serve</h4>
      <ul><li>Brookfield</li><li>Lakeside</li><li>Millbrook</li></ul>
      <div class="socials"><span></span><span></span><span></span><span></span></div>
      <div class="m-copy">© 2024 Hireway. All rights reserved.</div>
    </footer>
  </section>

  <!-- locations -->
  <section class="phone p4">
    <div class="m-top">Serving Employers &amp; Job Seekers</div>
    <div class="m-nav"><span class="m-brand">Hireway</span><span class="burger"><span></span><span></span><span></span></span></div>
    <div class="m-hero city" role="img" aria-label="Downtown street">
      <h2 class="center" style="top:90px">Our Locations</h2>
    </div>
    <div class="m-photo map" role="img" aria-label="Street map with office markers"></div>
    <div class="m-section">
      <h3>Office Locations</h3>
      <ul class="offices">
        <li><b>Brookfield Office</b>1420 Harbor Ave, Suite 200<br>1-800-555-0147</li>
        <li><b>Lakeside Office</b>87 Shoreline Dr, Unit 5<br>1-800-555-0162</li>
        <li><b>Millbrook Office</b>305 Mill St, Floor 2<br>1-800-555-0188</li>
        <li><b>Eastport Office</b>12 Dock Rd, Suite 9<br>1-800-555-0193</li>
      </ul>
    </div>
    <footer class="m-foot">
      <span class="m-brand">Hireway</span>
      <p>Trusted staffing partner for businesses and job seekers across the region.</p>
      <h4>Quick Links</h4>
      <ul><li>Home</li><li>Employers</li><li>Job Seekers</li><li>Locations</li><li>Contact Us</li></ul>
      <h4>Areas We Serve</h4>
      <ul><li>Brookfield</li><li>Lakeside</li><li>Millbrook</li></ul>
      <div class="socials"><span></span><span></span><span></span><span></span></div>
      <div class="m-copy">© 2024 Hireway. All rights reserved.</div>
    </footer>
  </section>

  <!-- single location -->
  <section class="phone p5">
    <div class="m-top">Serving Employers &amp; Job Seekers</div>
    <div class="m-nav"><span class="m-brand">Hireway</span><span class="burger"><span></span><span></span><span></span></span></div>
    <div class="m-hero office" role="img" aria-label="Open office interior">
      <h2 class="center" style="top:90px">Our Southern Office</h2>
    </div>
    <div class="m-photo map" role="img" aria-label="Street map with office marker"></div>
    <div class="m-section">
      <h3>Our Locations</h3>
      <ul class="offices">
        <li><b>Southern Office</b>640 Pine Ridge Rd, Suite 110<br>1-800-555-0175</li>
      </ul>
      <div class="m-center"><span class="m-btn">GET DIRECTIONS</span></div>
    </div>
    <footer class="m-foot">
      <span class="m-brand">Hireway</span>
      <p>Trusted staffing partner for businesses and job seekers across the region.</p>
      <h4>Quick Links</h4>
      <ul><li>Home</li><li>Employers</li><li>Job Seekers</li><li>Locations</li><li>Contact Us</li></ul>
      <h4>Areas We Serve</h4>
      <ul><li>Brookfield</li><li>Lakeside</li><li>Millbrook</li></ul>
      <div class="socials"><span></span><span></span><span></span><span></span></div>
      <div class="m-copy">© 2024 Hireway. All rights reserved.</div>
    </footer>
  </section>

</div>
</body>
</html>
```